" buscamos elaborar produtos saudáveis, isentos de glúten, lactose e açúcar. E utilizando ingredientes benéficos a nossa saúde, como fibra e gorduras boas (insaturadas). "

```html
<!DOCTYPE html>
<html lang="pt-BR">
<head>
<meta charset="utf-8">
<title>Sementes Vivas — Papel timbrado</title>
<link rel="stylesheet" href="https://fonts.googleapis.com/css2?family=Questrial&display=swap">
<style>
  :root {
    --backdrop: #e9e6e1;
    --paper: #ffffff;
    --brand-green: #7fa23a;
    --brand-orange: #ef7d22;
    --band-start: #ee6a24;
    --band-end: #f7b52d;
    --contact-text: #6f8f2e;
    --mark-tint-a: #f3f3f3;
    --mark-tint-b: #e9e9e9;
  }
  * { box-sizing: border-box; margin: 0; padding: 0; }
  html, body {
    width: 1200px; height: 1200px; overflow: hidden;
    background: var(--backdrop);
    font-family: "Questrial", sans-serif;
  }
  .letterhead {
    position: absolute; left: 240px; top: 54px;
    width: 720px; height: 1092px;
    background: var(--paper);
    box-shadow: 0 6px 24px rgba(0,0,0,0.18);
    overflow: hidden;
  }
  .brand {
    position: absolute; top: 96px; left: 0; right: 0;
    display: flex; align-items: center; justify-content: center; gap: 10px;
  }
  .brand-dot {
    width: 18px; height: 18px; border-radius: 50%;
    background: var(--brand-orange);
  }
  .brand-name {
    font-size: 28px; color: var(--brand-green); letter-spacing: 0.3px;
  }
  .background-mark {
    position: absolute; left: 0; top: 470px;
    width: 620px; height: 622px;
  }
  .contact {
    position: absolute; left: 300px; top: 930px;
    list-style: none;
    display: flex; flex-direction: column; gap: 6px;
  }
  .contact li {
    display: flex; align-items: center; gap: 9px;
    font-size: 12px; line-height: 14px; color: var(--contact-text);
  }
  .contact svg { width: 13px; height: 13px; flex: none; }
  .footer-band {
    position: absolute; left: 96px; bottom: 0;
    width: 528px; height: 24px;
    border-radius: 12px 12px 0 0;
    background: linear-gradient(90deg, var(--band-start), var(--band-end));
  }
</style>
</head>
<body>
  <main class="letterhead">
    <header class="brand">
      <span class="brand-dot"></span>
      <span class="brand-name">Sementes Vivas</span>
    </header>

    <svg class="background-mark" viewBox="0 0 620 622" role="img" aria-label="Marca da empresa em tom muito claro como marca d'água de fundo">
      <defs>
        <radialGradient id="markTint" cx="50%" cy="40%" r="55%">
          <stop offset="0%" stop-color="var(--mark-tint-b)"/>
          <stop offset="100%" stop-color="var(--mark-tint-a)"/>
        </radialGradient>
      </defs>
      <circle cx="300" cy="300" r="290" fill="url(#markTint)" opacity="0.75"/>
    </svg>

    <ul class="contact">
      <li>
        <svg viewBox="0 0 14 14"><rect width="14" height="14" rx="2" fill="var(--brand-green)"/><rect x="4.5" y="2.5" width="5" height="9" rx="1" fill="#fff"/></svg>
        21 90000-4172
      </li>
      <li>
        <svg viewBox="0 0 14 14"><rect width="14" height="14" rx="2" fill="var(--brand-green)"/><rect x="2.5" y="4" width="9" height="6" fill="#fff"/><path d="M2.5 4 L7 7.5 L11.5 4" stroke="var(--brand-green)" stroke-width="1" fill="none"/></svg>
        contato@sementesvivas.com
      </li>
      <li>
        <svg viewBox="0 0 14 14"><rect width="14" height="14" rx="2" fill="var(--brand-green)"/><circle cx="7" cy="7" r="4" stroke="#fff" stroke-width="1.2" fill="none"/><path d="M3 7 H11 M7 3 V11" stroke="#fff" stroke-width="1"/></svg>
        www.sementesvivas.com.br
      </li>
      <li>
        <svg viewBox="0 0 14 14"><rect width="14" height="14" rx="2" fill="var(--brand-green)"/></svg>
        social: /sementesvivas
      </li>
      <li>
        <svg viewBox="0 0 14 14"><rect width="14" height="14" rx="2" fill="var(--brand-green)"/></svg>
        sementesvivas
      </li>
    </ul>

    <div class="footer-band"></div>
  </main>
</body>
</html>
```